Detailed services rate card

We need a detailed rate card to promote our services to our customers.
The information is in the Word document dealrack-Rates-2015. Our customers are businesses that want to advertise their sales on our websites (http://www.dealrack-example.ca & http://www.lesrabais-example.ca

We would like a colorful but professional rate card. Please see our other rate card (dealrack-premium-2015-packages). The detailed rate card should have a design that fits this other rate card we are using.

```html
<!DOCTYPE html>
<html lang="en">
<head>
<meta charset="utf-8">
<title>dealrack – Detailed Rate Card 2015</title>
<link rel="stylesheet" href="https://fonts.googleapis.com/css2?family=Mulish:wght@400;700;800&family=Questrial&display=swap">
<style>
  :root{
    --ink:#000;
    --orange:#f79646;
    --amber:#ffc000;
    --flame:#ff6a13;
    --pink:#ff99ff;
    --row:#f2f2f2;
    --band:#a6a6a6;
    --paper:#f4f4f4;
    --paper-dark:#d9d9d9;
    --logo-bg:#000;
    --logo-ink:#ff6f8e;
  }
  *{box-sizing:border-box;margin:0;padding:0}
  html,body{width:848px;height:1200px;overflow:hidden;background:#fff}
  body{font-family:"Questrial",sans-serif;color:var(--ink)}
  .card{position:relative;width:848px;height:1200px;overflow:hidden}
  .doodle-backdrop{position:absolute;inset:0;background:linear-gradient(135deg,var(--paper),var(--paper-dark) 50%,var(--paper))}
  .brand{position:absolute;left:0;top:0;width:244px;height:103px;background:var(--logo-bg);display:flex;align-items:center;justify-content:center;gap:10px}
  .brand-dot{width:14px;height:14px;border-radius:50%;background:var(--logo-ink)}
  .brand-name{font-family:"Mulish",sans-serif;font-weight:800;font-size:40px;color:var(--logo-ink);letter-spacing:-1px}

  .rate-block{position:absolute;left:53px;width:744px;display:grid;border:2px solid var(--ink);background:var(--ink);gap:2px}
  .rate-block .label{display:flex;align-items:center;padding-left:8px;font-family:"Mulish",sans-serif;font-weight:700;font-size:35px;line-height:1.2}
  .rate-block .cell{background:var(--pink);display:flex;align-items:center;justify-content:center;text-align:center;font-size:13px;line-height:1.3}
  .label.orange{background:var(--orange)}
  .label.amber{background:var(--amber)}

  .regular{top:102px;height:113px;grid-template-columns:379px 174px 1fr;grid-template-rows:1fr 1fr}
  .regular .label{grid-row:span 2}
  .size-band{position:absolute;left:53px;top:220px;width:744px;height:27px;background:var(--band);font-family:"Mulish",sans-serif;font-weight:700;font-size:14px;display:flex;align-items:center;padding-left:6px}
  .bigbox{grid-template-columns:376px 181px 1fr;grid-template-rows:repeat(4,1fr)}
  .bigbox .label{grid-row:span 4}
  .bigbox-1{top:252px;height:121px}
  .bigbox-23{top:371px;height:121px}
  .email{top:506px;height:120px;grid-template-columns:376px 181px 1fr;grid-template-rows:repeat(4,1fr)}
  .email .label{grid-row:span 4}

  .section{position:absolute;left:53px;width:744px;border:2px solid var(--ink);background:var(--ink);display:grid;gap:2px}
  .section-title{grid-column:span 2;font-family:"Mulish",sans-serif;font-weight:700;font-size:28px;padding-left:8px;display:flex;align-items:center;height:38px}
  .section .item{background:var(--row);font-size:13.5px;line-height:1.3;padding:2px 6px;display:flex;align-items:center}
  .section .item em{font-style:italic}
  .section .price{background:var(--pink);font-size:13.5px;line-height:1.3;text-align:center;display:flex;align-items:center;justify-content:center}
  .services{top:641px;grid-template-columns:561px 1fr}
  .services .section-title{background:var(--amber)}
  .services .item,.services .price{min-height:27px}
  .long-term{top:914px;grid-template-columns:563px 1fr}
  .long-term .section-title{background:var(--flame)}
  .long-term .item,.long-term .price{height:47px}
  .design{top:1066px;grid-template-columns:569px 1fr}
  .design .section-title{background:var(--amber)}
  .design .item,.design .price{height:48px}
  .design .item{text-align:justify}

  .footnote{position:absolute;left:356px;top:1168px;width:444px;height:20px;background:var(--band);font-size:11.5px;font-style:italic;display:flex;align-items:center;justify-content:center}
</style>
</head>
<body>
<main class="card">
  <div class="doodle-backdrop" role="img" aria-label="Background of hand-drawn web and communication doodles in black and white"></div>

  <header class="brand">
    <span class="brand-dot"></span>
    <span class="brand-name">dealrack</span>
  </header>

  <section class="rate-block regular">
    <div class="label orange">Regular Ad</div>
    <div class="cell">1 day to<br>2 weeks</div>
    <div class="cell">$110<br>Minimum fee</div>
    <div class="cell">3 weeks to 1 month</div>
    <div class="cell">$145</div>
  </section>

  <div class="size-band">Big box (300X250 pixels)</div>

  <section class="rate-block bigbox bigbox-1">
    <div class="label amber">Big box #1</div>
    <div class="cell">1 week</div><div class="cell">$150</div>
    <div class="cell">2 weeks</div><div class="cell">$200</div>
    <div class="cell">3 weeks</div><div class="cell">$275</div>
    <div class="cell">4 weeks</div><div class="cell">$325</div>
  </section>

  <section class="rate-block bigbox bigbox-23">
    <div class="label amber">Big box #2 &amp; #3</div>
    <div class="cell">1 week</div><div class="cell">$125</div>
    <div class="cell">2 weeks</div><div class="cell">$175</div>
    <div class="cell">3 weeks</div><div class="cell">$250</div>
    <div class="cell">4 weeks</div><div class="cell">$300</div>
  </section>

  <section class="rate-block email">
    <div class="label orange">Targeted email<br>advertising</div>
    <div class="cell">10,000 to 14,999 emails</div><div class="cell">$40 CPM</div>
    <div class="cell">15,000 to 19,999 emails</div><div class="cell">$35 CPM</div>
    <div class="cell">20,000 to 24,999 emails</div><div class="cell">$30 CPM</div>
    <div class="cell">25,000+ emails</div><div class="cell">$25 CPM</div>
  </section>

  <section class="section services">
    <h2 class="section-title">Other Services</h2>
    <div class="item"><span>VIP Sale <em>(Your visual will appear at the top our newsletter, and 1 post Friendspace/ Chirper)</em></span></div>
    <div class="price">$50</div>
    <div class="item">dealrack.ca Squad: coverage of your sale on Chirper and Friendspace</div>
    <div class="price">$300 per day</div>
    <div class="item">Sponsored blog post on dealrack.ca’s blog</div>
    <div class="price">$150</div>
    <div class="item">Video of your sale or store (posted only on dealrack.ca/lesrabais.ca’s website)</div>
    <div class="price">$300</div>
    <div class="item">Video of your sale or store (Video file provided and copyrights to use as you wish)</div>
    <div class="price">$400</div>
    <div class="item">Professional photo shoot (combined with a filming shoot)</div>
    <div class="price">$100</div>
    <div class="item">Professional photo shoot</div>
    <div class="price">$200</div>
  </section>

  <section class="section long-term">
    <h2 class="section-title">Long-term Agreements</h2>
    <div class="item">6 months: you pay the first 5 months and the 6th month is free.<br>Payable in 3 instalments.</div>
    <div class="price">$725<br>($120.83/month)</div>
    <div class="item">12 months: get a 20% discount and save $350.<br>Payable in 3 instalments.</div>
    <div class="price">$1,390<br>($115.83/month)</div>
  </section>

  <section class="section design">
    <h2 class="section-title">Graphic Design</h2>
    <div class="item">Graphic design - flyer / small photo / big box or other. The price varies depending on the complexity of the work (ex: photo editing, visual research, etc.).</div>
    <div class="price">$50 - $200</div>
  </section>

  <p class="footnote">*January 2015. Prices are subject to change without prior notice.</p>
</main>
</body>
</html>
```